When the boots match march on! book cover design

Book cover for a business, non-fiction book.
About stepping up, being who you truly are, and willing not to fit in.

TITLE: When The Boots Match, March On!
SUBTITLE: Quit copying the chief others expect of you and begin shaping the chief nobody else could ever shape...
AUTHOR: Tobias Hartwell-Brenner
Updates

we never uploaded the brief

Target Market(s)

Business people, curious leaders, insiders who have a secret itch to be an outsider
AGE: 35-50 years old

Font styles to use
Sans Serif
Other font styles liked:
• designer's choice!

Requirements
Must have
• Very visual
Imagery must reflect the topic of the book

```html
<!DOCTYPE html>
<html lang="en">
<head>
<meta charset="utf-8">
<title>When The Boots Match, March On! — Book Cover</title>
<link rel="stylesheet" href="https://fonts.googleapis.com/css2?family=Montserrat:ital,wght@0,100;0,900;1,800&display=swap">
<style>
  :root {
    --paper: #ffffff;
    --ink: #0d0d0d;
    --band-red: #a61b1d;
    --cape-red-light: #e8251f;
    --cape-red-dark: #9e1316;
    --band-text: #ffffff;
  }
  html, body {
    margin: 0;
    padding: 0;
    overflow: hidden;
    background: var(--paper);
  }
  .cover {
    position: relative;
    width: 849px;
    height: 1200px;
    background: var(--paper);
    overflow: hidden;
    font-family: "Montserrat", sans-serif;
    color: var(--ink);
  }
  .author {
    position: absolute;
    top: 76px;
    left: 0;
    width: 100%;
    margin: 0;
    text-align: center;
    font-weight: 900;
    font-size: 33px;
    letter-spacing: 0.5px;
    line-height: 1;
  }
  .title {
    margin: 0;
    font-weight: 100;
  }
  .title-line {
    position: absolute;
    left: 0;
    width: 100%;
    text-align: center;
    line-height: 1;
    white-space: nowrap;
  }
  .title-line--first {
    top: 305px;
    font-size: 104px;
    font-weight: 100;
    letter-spacing: 2px;
  }
  .title-line--second {
    top: 420px;
    font-size: 76px;
    font-weight: 100;
    letter-spacing: 1px;
  }
  .title-strong {
    font-weight: 900;
  }
  .title-band {
    position: absolute;
    top: 520px;
    left: 106px;
    width: 646px;
    height: 128px;
    background: var(--band-red);
    display: flex;
    align-items: center;
    justify-content: center;
    color: var(--band-text);
    font-weight: 900;
    font-size: 80px;
    line-height: 1;
    letter-spacing: 1px;
    white-space: nowrap;
  }
  .boots-artwork {
    position: absolute;
    top: 720px;
    left: 78px;
    width: 690px;
    height: 192px;
  }
  .subtitle {
    position: absolute;
    top: 970px;
    left: 0;
    width: 100%;
    margin: 0;
    text-align: center;
    font-style: italic;
    font-weight: 800;
    font-size: 15px;
    line-height: 1.75;
    text-transform: uppercase;
  }
</style>
</head>
<body>
  <main class="cover">
    <p class="author">TOBIAS HARTWELL-BRENNER</p>

    <h1 class="title">
      <span class="title-line title-line--first">WHEN THE</span>
      <span class="title-line title-line--second">BOOTS <span class="title-strong">MATCH,</span></span>
      <span class="title-band">MARCH ON!</span>
    </h1>

    <svg class="boots-artwork" viewBox="0 0 690 192" role="img" aria-label="Row of red hero boots illustration">
      <defs>
        <linearGradient id="bootsGradient" x1="0" y1="0" x2="1" y2="1">
          <stop offset="0" stop-color="var(--cape-red-dark)"/>
          <stop offset="0.5" stop-color="var(--cape-red-light)"/>
          <stop offset="1" stop-color="var(--cape-red-dark)"/>
        </linearGradient>
      </defs>
      <rect x="0" y="0" width="690" height="192" rx="18" fill="url(#bootsGradient)"/>
    </svg>

    <p class="subtitle">
      Quit copying the chief others expect of you and begin<br>
      shaping the chief nobody else could ever shape...
    </p>
  </main>
</body>
</html>
```